Real Estate 24"x24" Sign, Business Card, Letter Head and Envelope

This is a 4 project contest. If we choose a design or designs we like from what you sent we are willing to pay an amount at our discretion for that design even if we don't like all your designs for the 4 projects. Please be creative. Attached are our logo files. Please message us with any questions. Thanks and Good Luck!
Project 1: QLTV Realty 24" x 24" yard sign
We want to use the same blue background in our logo for the sign where the logo in white font will be on. CMYK 100,80,0,0. Attached is a sample a local designer made for you to get an idea what we are looking for. In the sample, the website is way too big and the entire sign is very plain and not attractive looking plus blue color is wrong one. We want the logo on top as large as possible but keeping it proportionate and attractive looking buy not too big that it looks odd. The following information can go in white color background or same blue color background color. Our company colors are blue (as per logo), green (as per logo), and white. "Residential & Commercial" goes under the logo. Under that put our phone number "312-948-6051" as large as possible but still looks good and under that our website in much smaller but readable font "www.qltvrealty.com".
Project 2: Envelope
We have two version of the logo. Use one or both. Whatever looks best in your design. The envelope will be white. We only want on top left corner logo and underneath our mailing address: 5197 Larchmere Ave. Skokie, IL 60093-1725. Maybe some creative decorative design at bottom of envelope will look nice
Project 3: Letter Head
We have two version of the logo. Use one or both. Whatever looks best in your design. We want the following information on the top of the letterhead. Logo, address: 5197 Larchmere Ave., Skokie, IL 60093-1725, phone: 312-948-6051, fax: 312-682-9307 website www.qltvrealty.com, email: info@qltvrealty.com
Project 4: Business card
Use either logo. We need cards for two individuals. Information for Person 1: Dev Kulkarni, Managing Broker, Phone: 312-948-6051, Email: dev.kulkarni@qltvrealty.com. Person 2: Ajay Kulkarni Broker Phone: 312-519-8263 Email: ajay.kulkarni@qltvrealty.com. Add Address, Fax and website same as above letter head.

```html
<!DOCTYPE html>
<html lang="en">
<head>
<meta charset="utf-8">
<title>QLTV Realty – Business Card Front and Back</title>
<link rel="stylesheet" href="https://fonts.googleapis.com/css2?family=Open+Sans:wght@400;600;700&display=swap">
<style>
  :root {
    --brand-blue: #0d4ca1;
    --brand-green: #6abf45;
    --card-white: #ffffff;
    --stage-dark: #1f1f20;
    --label-white: #f4f4f4;
  }
  * { margin: 0; padding: 0; box-sizing: border-box; }
  html, body {
    width: 1200px;
    height: 999px;
    overflow: hidden;
    background: var(--stage-dark);
    font-family: "Open Sans", Arial, sans-serif;
  }
  .board { position: relative; width: 1200px; height: 999px; }

  .card {
    position: absolute;
    width: 742px;
    height: 424px;
    background: var(--card-white);
    overflow: hidden;
  }
  .card--front { left: 45px; top: 62px; }
  .card--back { left: 415px; top: 518px; }
  .card__wave { position: absolute; left: 0; top: 0; width: 742px; height: 424px; }

  .brand {
    position: absolute;
    display: flex;
    align-items: center;
    gap: 14px;
    font-weight: 700;
    font-size: 50px;
    letter-spacing: 1px;
    white-space: nowrap;
  }
  .brand__mark { width: 26px; height: 26px; }
  .card--front .brand { left: 0; right: 0; justify-content: center; top: 90px; color: var(--card-white); }
  .card--front .brand__mark { background: var(--card-white); }
  .card--back .brand { left: 0; right: 0; justify-content: center; top: 196px; color: var(--brand-blue); }
  .card--back .brand__mark { background: var(--brand-blue); }

  .person { position: absolute; left: 37px; top: 340px; color: var(--brand-blue); }
  .person__name { font-weight: 700; font-size: 24px; line-height: 1.1; }
  .person__title { font-size: 17px; margin-top: 6px; }

  .contact { position: absolute; left: 441px; top: 305px; list-style: none; color: var(--brand-blue); }
  .contact__item { display: flex; align-items: center; height: 24.5px; font-size: 18px; }
  .contact__icon { width: 18px; height: 18px; margin-right: 18px; fill: var(--brand-blue); }

  .label {
    position: absolute;
    color: var(--label-white);
    font-size: 45px;
    line-height: 60px;
    font-weight: 400;
  }
  .label--front { left: 841px; top: 253px; }
  .label--back { left: 139px; top: 708px; }
</style>
</head>
<body>
<main class="board">

  <section class="card card--front" aria-label="Business card front">
    <svg class="card__wave" viewBox="0 0 742 424" aria-hidden="true">
      <path d="M0 243 C90 264 200 283 330 289 C470 294 610 270 742 238 V200 H0 Z" fill="var(--brand-green)"/>
      <path d="M0 0 H742 V220 C610 258 460 287 330 286 C200 284 90 263 0 243 Z" fill="var(--brand-blue)"/>
    </svg>
    <div class="brand"><span class="brand__mark"></span>QLTV Realty</div>
    <div class="person">
      <p class="person__name">Dev Kulkarni</p>
      <p class="person__title">Managing Broker</p>
    </div>
    <ul class="contact">
      <li class="contact__item">
        <svg class="contact__icon" viewBox="0 0 24 24"><path d="M6.6 10.8a15 15 0 0 0 6.6 6.6l2.2-2.2a1 1 0 0 1 1-.25 11.4 11.4 0 0 0 3.6.57 1 1 0 0 1 1 1V20a1 1 0 0 1-1 1A17 17 0 0 1 3 4a1 1 0 0 1 1-1h3.5a1 1 0 0 1 1 1c0 1.25.2 2.45.57 3.57a1 1 0 0 1-.25 1z"/></svg>
        312-948-6051
      </li>
      <li class="contact__item">
        <svg class="contact__icon" viewBox="0 0 24 24"><path d="M7 2h8l3 3v5H7z M3 11h18v9H3z M6 14h4v2H6z"/></svg>
        312-682-9307
      </li>
      <li class="contact__item">
        <svg class="contact__icon" viewBox="0 0 24 24"><path d="M2 9l10-7 10 7v12H2z M4 10l8 6 8-6" /><path d="M4 10l8 6 8-6" fill="none" stroke="#fff" stroke-width="1.6"/></svg>
        dev.kulkarni@qltvrealty.com
      </li>
      <li class="contact__item">
        <svg class="contact__icon" viewBox="0 0 24 24" fill="none" stroke="var(--brand-blue)" stroke-width="1.8"><circle cx="12" cy="12" r="9"/><ellipse cx="12" cy="12" rx="4" ry="9"/><path d="M3 12h18M5 7h14M5 17h14"/></svg>
        qltvrealty.com
      </li>
    </ul>
  </section>

  <section class="card card--back" aria-label="Business card back">
    <svg class="card__wave" viewBox="0 0 742 424" aria-hidden="true">
      <path d="M0 52 C110 80 250 98 370 97 C500 96 620 82 742 60 V0 H0 Z" fill="var(--brand-green)"/>
      <path d="M0 0 H742 V30 C620 65 490 93 370 95 C250 96 110 78 0 52 Z" fill="var(--brand-blue)"/>
    </svg>
    <div class="brand"><span class="brand__mark"></span>QLTV Realty</div>
  </section>

  <p class="label label--front">B Card<br>Front</p>
  <p class="label label--back">B Card<br>Back</p>

</main>
</body>
</html>
```